Children's Educational Software - Login Screens

We need graphics for some basic login pages. The main requirements are a background image, buttons and background overlay (box for login fields and app icons). Must utilize responsive design for various resolutions and devices. The mock-up file provides an example of the direction we are wanting to go. The app page will require a version of the background that extends down using a solid colour. One idea would be to add some flowers, bees, etc. to help add some life to the bottom half. I like the idea of clouds and grass, but am open to anything.

Target Market(s)

Elementary teachers and young children

Coding

Coded - Design and coding required

Number of Pages Required

2 page

Font styles to use
Sans Serif

Requirements
Must have
• Responsive design for various resolutions and devices
Nice to have
• clouds, grass, new app icons if current icons don't fit with new design

```html
<!DOCTYPE html>
<html lang="en">
<head>
<meta charset="utf-8">
<title>BrightSteps – School Login</title>
<link rel="stylesheet" href="https://fonts.googleapis.com/css2?family=Roboto:wght@400;500;700&family=Open+Sans:wght@600&display=swap">
<style>
  :root {
    --sky-top: #a9d3f2;
    --sky-mid: #cbe6f5;
    --horizon: #8fd3e6;
    --grass-light: #9fd23c;
    --grass-dark: #7fb82a;
    --brand: #2f4a94;
    --panel-rim: rgba(226, 240, 200, 0.85);
    --panel: #31447f;
    --panel-top: #354a8a;
    --white: #ffffff;
    --field: #f4f4f4;
    --admin-top: #95d31a;
    --admin-bottom: #5fa30e;
    --teacher-top: #e0141c;
    --teacher-bottom: #a8060c;
    --student-top: #1b8ed8;
    --student-bottom: #0b62b0;
    --tile-rim: #d7dce4;
    --footer: #1e3178;
  }
  * { box-sizing: border-box; margin: 0; padding: 0; }
  html, body { width: 1200px; height: 813px; overflow: hidden; }
  body {
    position: relative;
    font-family: "Roboto", Arial, sans-serif;
    color: var(--white);
  }
  .scene {
    position: absolute; inset: 0 0 49px 0;
    background: linear-gradient(180deg, var(--sky-top) 0%, var(--sky-mid) 38%, var(--horizon) 62%, var(--grass-light) 72%, var(--grass-dark) 100%);
  }
  .brand {
    position: absolute; left: 38px; top: 62px;
    display: flex; align-items: center; gap: 14px;
  }
  .brand-mark {
    width: 72px; height: 72px; border-radius: 8px; background: var(--brand);
  }
  .brand-name {
    font-family: "Open Sans", Arial, sans-serif; font-weight: 600;
    font-size: 50px; color: var(--brand); letter-spacing: -1px;
  }
  .login-frame {
    position: absolute; left: 317px; top: 193px; width: 584px; height: 479px;
    background: var(--panel-rim); border-radius: 12px;
  }
  .login-panel {
    position: absolute; left: 330px; top: 206px; width: 559px; height: 453px;
    border-radius: 12px;
    background: linear-gradient(160deg, var(--panel-top) 0%, var(--panel) 60%);
  }
  .title {
    position: absolute; left: 470px; top: 248px; display: flex; align-items: center; gap: 18px;
  }
  .title h1 { font-size: 38px; font-weight: 500; letter-spacing: 0.5px; }
  .field-label { position: absolute; left: 469px; top: 331px; font-size: 11px; font-weight: 500; }
  .field {
    position: absolute; left: 530px; top: 314px; width: 207px; height: 43px;
    border-radius: 3px; background: linear-gradient(180deg, #e6e6e6, var(--white) 45%, #eeeeee);
    border: none;
  }
  .link { position: absolute; font-size: 11px; font-weight: 500; color: var(--white); text-decoration: underline; }
  .find-id { left: 591px; top: 371px; }
  .pick-list { left: 461px; top: 424px; }
  .checkbox {
    position: absolute; left: 431px; top: 422px; width: 18px; height: 18px;
    border-radius: 2px; background: linear-gradient(180deg, #fff, #d9d9d9);
  }
  .role {
    position: absolute; top: 478px; width: 88px; text-align: center;
  }
  .role-tile {
    width: 88px; height: 84px; border-radius: 16px; border: 3px solid var(--tile-rim);
    display: flex; align-items: center; justify-content: center;
  }
  .role-name { display: block; margin-top: 8px; font-size: 11.5px; font-weight: 500; }
  .role-admin { left: 454px; }
  .role-teacher { left: 567px; }
  .role-student { left: 681px; }
  .role-admin .role-tile { background: linear-gradient(180deg, var(--admin-top), var(--admin-bottom)); }
  .role-teacher .role-tile { background: linear-gradient(180deg, var(--teacher-top), var(--teacher-bottom)); }
  .role-student .role-tile { background: linear-gradient(180deg, var(--student-top), var(--student-bottom)); }
  .help-links { position: absolute; left: 507px; top: 619px; display: flex; gap: 14px; font-size: 11.5px; }
  .help-links a { color: var(--white); font-weight: 500; }
  .footer {
    position: absolute; left: 0; bottom: 0; width: 1200px; height: 49px;
    background: var(--footer); display: flex; align-items: center; justify-content: space-between;
    padding: 0 62px 0 66px; font-size: 14px; font-weight: 500;
  }
  .contact { display: flex; gap: 14px; }
</style>
</head>
<body>
  <div class="scene" role="img" aria-label="Sunny meadow scene: blue sky with sun and clouds, green hills with trees, and a boy reading a book among stacks of books"></div>

  <header class="brand">
    <span class="brand-mark"></span>
    <span class="brand-name">BrightSteps</span>
  </header>

  <div class="login-frame"></div>
  <main class="login-panel"></main>

  <div class="title">
    <svg width="44" height="44" viewBox="0 0 44 44" aria-hidden="true">
      <circle cx="20" cy="12" r="9" fill="#fff"/>
      <path d="M3 42c0-11 8-17 17-17s17 6 17 17z" fill="#fff"/>
      <circle cx="35" cy="36" r="8" fill="#fff" stroke="#31447f" stroke-width="2"/>
      <rect x="31.5" y="35" width="7" height="5" fill="#31447f"/>
      <path d="M33 35v-2a2 2 0 0 1 4 0v2" fill="none" stroke="#31447f" stroke-width="1.5"/>
    </svg>
    <h1>School Login</h1>
  </div>

  <label class="field-label" for="school-id">School ID</label>
  <input class="field" id="school-id" type="text" aria-label="School ID">
  <a class="link find-id" href="#">Find my School id</a>

  <span class="checkbox"></span>
  <a class="link pick-list" href="#">Pick Students from a list</a>

  <a class="role role-admin" href="#">
    <span class="role-tile">
      <svg width="50" height="50" viewBox="0 0 50 50" aria-hidden="true">
        <circle cx="20" cy="13" r="9" fill="#fff"/>
        <path d="M4 44c0-12 7-18 16-18 5 0 9 2 12 5v13z" fill="#fff"/>
        <circle cx="37" cy="37" r="8" fill="none" stroke="#fff" stroke-width="5" stroke-dasharray="3 2.3"/>
        <circle cx="37" cy="37" r="5" fill="none" stroke="#fff" stroke-width="3"/>
      </svg>
    </span>
    <span class="role-name">Admin</span>
  </a>

  <a class="role role-teacher" href="#">
    <span class="role-tile">
      <svg width="54" height="54" viewBox="0 0 54 54" aria-hidden="true">
        <circle cx="22" cy="13" r="9" fill="#fff"/>
        <path d="M6 44c0-12 7-19 16-19s16 7 16 19z" fill="#fff"/>
        <rect x="10" y="32" width="24" height="14" fill="#c20d13" stroke="#fff" stroke-width="2"/>
        <line x1="22" y1="32" x2="22" y2="46" stroke="#fff" stroke-width="2"/>
        <line x1="36" y1="36" x2="48" y2="10" stroke="#fff" stroke-width="3" stroke-linecap="round"/>
      </svg>
    </span>
    <span class="role-name">Teacher</span>
  </a>

  <a class="role role-student" href="#">
    <span class="role-tile">
      <svg width="50" height="50" viewBox="0 0 50 50" aria-hidden="true">
        <path d="M11 10l14-6 14 6-14 6z" fill="#fff"/>
        <circle cx="25" cy="19" r="9" fill="#fff"/>
        <path d="M6 46c0-11 8-17 19-17s19 6 19 17z" fill="#fff"/>
        <path d="M20 30l5 8 5-8" fill="none" stroke="#1475c4" stroke-width="2"/>
      </svg>
    </span>
    <span class="role-name">Student</span>
  </a>

  <nav class="help-links">
    <a href="#">Quick Start Guide</a>
    <span>|</span>
    <a href="#">Support Page</a>
  </nav>

  <footer class="footer">
    <span>Copyright © 2019 BrightSteps. All Right Reserved</span>
    <span class="contact">
      <span>1-800-555-0142</span>
      <span>|</span>
      <span>help@brightsteps.com</span>
    </span>
  </footer>
</body>
</html>
```